"Brightwall Sound Living Residences" need a busines Card Design got Builder

We need a business card design for a company based in Milford, Michigancalled Brightwall Sound Living Residences - has been recognized as a premier custom home builder. Distinguished by outstanding craftmanship and timeless beauty. Our custom home can be found in the most prestigious communities in Michigan. The homes are built with ICF (insulated concrete homes) which is green, allergy free, fire free, mold free and quitter. Our slogan "building one dream at a Time" and also we are ICF distributor for the state of Michigan

Target Market(s)

Anyone who is making over $100,000 a year and who wants to have totally custom built home. Ages from 29 up to 60 years old

Industry/Entity Type

Concrete

Contact Information for Business Card

we want to use - green, black, gray or blue colors - we want to look different with our business cards, because we built homes only with ICF, green, healthier and highly energy efficient homes.

Requirements
Must have
• I have logo that I attached and we have been using the logo (the only green home)
Nice to have
• should look quality business card,

Files

```html
<!DOCTYPE html>
<html lang="en">
<head>
<meta charset="utf-8">
<title>Brightwall Sound Living Residences – Business Card</title>
<link rel="stylesheet" href="https://fonts.googleapis.com/css2?family=Lato:wght@300;400;700&display=swap">
<style>
  :root {
    --backdrop: #e9e6e1;
    --card: #ffffff;
    --ink-grey: #8d9197;
    --mark: #7a74a8;
    --sky: #3d95cf;
    --sky-deep: #1f7fc4;
    --indigo: #3b3673;
    --badge: #b9bcc0;
    --white: #ffffff;
  }
  * { box-sizing: border-box; margin: 0; padding: 0; }
  html, body {
    width: 1200px; height: 900px; overflow: hidden;
    background: var(--backdrop);
    font-family: "Lato", sans-serif;
  }
  .card {
    position: absolute; left: 180px; top: 210px;
    width: 840px; height: 480px;
    background: var(--card);
    box-shadow: 0 10px 30px rgba(0,0,0,.18);
    overflow: hidden;
  }
  .brand {
    position: absolute; left: 70px; top: 52px;
    display: flex; align-items: center; gap: 26px;
  }
  .brand-dot {
    width: 140px; height: 140px; border-radius: 50%;
    background: var(--mark);
  }
  .brand-name {
    font-weight: 300; color: var(--ink-grey);
    font-size: 36px; line-height: 1.02; letter-spacing: 1px;
    text-transform: uppercase;
  }
  .partner-badge {
    position: absolute; right: 36px; top: 26px;
    width: 46px; height: 46px; background: var(--badge);
  }
  .person {
    position: absolute; left: 0; top: 262px;
    width: 400px; height: 158px;
    background: linear-gradient(135deg, var(--sky), var(--sky-deep));
    color: var(--white); text-align: center;
    display: flex; flex-direction: column; justify-content: center;
    padding-right: 40px;
  }
  .person::before {
    content: ""; position: absolute; left: 150px; top: -12px;
    border-left: 12px solid transparent; border-right: 12px solid transparent;
    border-bottom: 12px solid var(--sky);
  }
  .person-name { font-size: 36px; font-weight: 400; }
  .person-role { font-size: 17px; letter-spacing: 1px; margin-top: 2px; }
  .contact {
    position: absolute; left: 408px; top: 192px; right: 0;
    height: 204px; background: var(--indigo);
    color: var(--white);
    padding: 44px 0 0 58px;
    list-style: none;
  }
  .contact::before {
    content: ""; position: absolute; left: 0; top: 118px;
    border-top: 12px solid transparent; border-bottom: 12px solid transparent;
    border-left: 14px solid var(--white);
  }
  .contact li {
    display: flex; align-items: center; gap: 14px;
    font-size: 24px; line-height: 30px;
  }
  .contact svg { width: 18px; height: 18px; flex: none; fill: none; stroke: var(--white); stroke-width: 2; }
  .slogan {
    position: absolute; left: 0; width: 640px; top: 432px;
    text-align: center; color: var(--sky-deep);
    font-weight: 700; font-size: 20px; letter-spacing: 4px;
    text-transform: uppercase;
  }
</style>
</head>
<body>
  <article class="card">
    <header class="brand">
      <span class="brand-dot"></span>
      <p class="brand-name">Brightwall Sound<br>Living Residences</p>
    </header>
    <span class="partner-badge" aria-label="Partner badge"></span>

    <section class="person">
      <p class="person-name">Daniel Reyes</p>
      <p class="person-role">DIRECTOR</p>
    </section>

    <ul class="contact">
      <li><svg viewBox="0 0 24 24"><path d="M5 3h4l2 5-3 2a12 12 0 0 0 6 6l2-3 5 2v4a2 2 0 0 1-2 2A18 18 0 0 1 3 5a2 2 0 0 1 2-2z"/></svg>450 61 204</li>
      <li><svg viewBox="0 0 24 24"><rect x="6" y="3" width="12" height="6"/><rect x="3" y="9" width="18" height="8"/><rect x="7" y="14" width="10" height="7"/></svg>450 61 208</li>
      <li><svg viewBox="0 0 24 24"><rect x="3" y="5" width="18" height="14"/><path d="M3 5l9 8 9-8"/></svg>dreyes@brightwall-living.com</li>
      <li><svg viewBox="0 0 24 24"><circle cx="12" cy="12" r="9"/><path d="M3 12h18M12 3a14 14 0 0 1 0 18M12 3a14 14 0 0 0 0 18"/></svg>www.brightwall-living.com</li>
    </ul>

    <p class="slogan">Building one dream at a time</p>
  </article>
</body>
</html>
```